Quickset Remote Screening Lunch and Learn Event Flyer

We are hosting a lunch and learn for prospects to introduce our Digital Interview process - attendees are Human Resource and Hiring Managers.

We need a flyer that we can email and also have printed (large postcard size) to be either mailed out or dropped off at a prospects location. I have included a picture of a Digital Interview to be used on the flyer (people don't get it till they see it) as well as content. Please feel free to rewrite, restructure, the content to produce a good flow.

Return address on the back (the one we would print) is RL Staffing - 2740 Lorvane Court - Suite 318 - Nashville, TN 37490

Target Market(s)

Business Owners, Human Resource Managers

Industry/Entity Type

Digital

Font styles to use
Sans Serif

Requirements
Must have
• Must be clean and professional with plenty of white space

```html
<!DOCTYPE html>
<html lang="en">
<head>
<meta charset="utf-8">
<title>Quickset Remote Screening – Lunch and Learn Flyer</title>
<link href="https://fonts.googleapis.com/css2?family=Open+Sans:wght@300;400;700;800&family=Arimo:wght@400;700&display=swap" rel="stylesheet">
<style>
  :root{
    --stage:#ebe7e3;
    --paper:#ffffff;
    --red-deep:#a93c45;
    --red:#c4545b;
    --pink:#e68a88;
    --pink-soft:#f2b3ae;
    --ink:#2b2b2b;
    --ink-soft:#4a4a4a;
    --photo-light:#e9ebee;
    --photo-mid:#b9bec6;
  }
  *{margin:0;padding:0;box-sizing:border-box}
  html,body{width:1200px;height:1080px;overflow:hidden}
  body{background:var(--stage);font-family:"Arimo",Arial,sans-serif;color:var(--ink);position:relative}

  .flyer{position:absolute;top:180px;width:540px;height:720px;background:var(--paper);overflow:hidden;box-shadow:0 6px 24px rgba(0,0,0,.18)}
  .flyer--front{left:40px}
  .flyer--back{left:620px}
  .flyer svg.shapes{position:absolute;inset:0;width:540px;height:720px}

  /* front */
  .brand{position:absolute;left:36px;top:44px;display:flex;align-items:center;gap:10px;font-family:"Open Sans",sans-serif;font-weight:700;font-size:22px;color:var(--red-deep)}
  .brand-mark{width:14px;height:14px;background:var(--red-deep)}
  .headline{position:absolute;left:36px;right:30px;bottom:62px;color:#fff;font-family:"Open Sans",sans-serif}
  .headline-main{font-weight:800;font-size:38px;letter-spacing:.5px;line-height:1.1}
  .headline-sub{font-weight:300;font-size:23px;letter-spacing:1px;margin-top:8px}

  /* back */
  .intro{position:absolute;left:36px;top:40px;width:410px;font-size:15.5px;line-height:1.45;color:var(--ink)}
  .intro p{text-indent:40px}
  .event{position:absolute;left:36px;top:232px;font-size:11px;color:var(--red-deep);line-height:1.9}
  .event-line{display:flex;align-items:center;gap:8px}
  .event svg{width:12px;height:12px}
  .benefits{position:absolute;left:70px;top:292px}
  .benefits h2,.purpose h2{font-family:"Open Sans",sans-serif;font-weight:700;font-size:15px;letter-spacing:.3px}
  .benefits h2{color:var(--ink-soft)}
  .benefits ul{list-style:none;margin:14px 0 0 20px;font-size:12px;color:var(--ink-soft);line-height:2.05}
  .purpose{position:absolute;left:70px;top:560px;width:270px;color:#fff}
  .purpose h2{color:var(--ink-soft)}
  .purpose p{font-size:13px;line-height:1.35;margin-top:8px;padding-left:14px}
  .contact{position:absolute;right:30px;bottom:28px;text-align:right;color:#fff}
  .contact .email{font-size:12px}
  .contact .phone{font-size:16px;margin-top:4px}
  .contact-rule{position:absolute;right:30px;width:250px;height:1px;background:#fff}
</style>
</head>
<body>

<section class="flyer flyer--front">
  <svg class="shapes" viewBox="0 0 540 720" aria-hidden="false">
    <defs>
      <linearGradient id="photoTone" x1="0" y1="0" x2="1" y2="1">
        <stop offset="0" stop-color="var(--photo-light)"/>
        <stop offset="1" stop-color="var(--photo-mid)"/>
      </linearGradient>
      <linearGradient id="bandTone" x1="0" y1="0" x2="1" y2="1">
        <stop offset="0" stop-color="#e4a6a3"/>
        <stop offset="1" stop-color="#d76f6e"/>
      </linearGradient>
    </defs>
    <rect x="0" y="120" width="540" height="470" fill="url(#photoTone)" role="img" aria-label="Photo of a hiring manager at a desk reviewing a video interview on a laptop"/>
    <polygon points="400,0 540,0 540,150" fill="var(--pink)" opacity=".85"/>
    <polygon points="0,470 540,380 540,720 0,720" fill="url(#bandTone)" opacity=".88"/>
    <polygon points="150,720 540,440 540,720" fill="var(--red)" opacity=".35"/>
    <polygon points="0,560 330,720 0,720" fill="var(--pink-soft)" opacity=".5"/>
  </svg>
  <div class="brand"><span class="brand-mark"></span>RL Staffing</div>
  <div class="headline">
    <div class="headline-main">HOW DIGITAL INTERVIEWS</div>
    <div class="headline-sub">CAN PRODUCE BETTER CANDIDATES</div>
  </div>
</section>

<section class="flyer flyer--back">
  <svg class="shapes" viewBox="0 0 540 720">
    <defs>
      <linearGradient id="backRed" x1="0" y1="0" x2="0" y2="1">
        <stop offset="0" stop-color="var(--red-deep)"/>
        <stop offset=".7" stop-color="var(--red)"/>
        <stop offset="1" stop-color="var(--pink)"/>
      </linearGradient>
    </defs>
    <rect width="540" height="720" fill="url(#backRed)"/>
    <polygon points="0,0 460,0 330,560 0,545" fill="var(--paper)"/>
    <polygon points="0,545 330,560 0,720" fill="var(--pink)" opacity=".35"/>
  </svg>

  <div class="intro"><p>Quickset Remote Screening offers individuals the ability to share their stories and demonstrate their work through video – all on their own time by using a PC, Laptop or Smartphone. More than 60% of interviews take place outside of the normal 9-5 business hours. Learn how Hiring Managers can save time, qualify more candidates, and can get a better overall first impression before setting up a first round interview.</p></div>

  <div class="event">
    <div class="event-line">
      <svg viewBox="0 0 12 12"><path d="M6 0.5a4 4 0 0 0-4 4c0 3 4 7 4 7s4-4 4-7a4 4 0 0 0-4-4z" fill="var(--red-deep)"/><circle cx="6" cy="4.5" r="1.5" fill="#fff"/></svg>
      RL Staffing - 2740 Lorvane Court - Suite 318 - Nashville, TN 37490
    </div>
    <div class="event-line">
      <svg viewBox="0 0 12 12"><circle cx="6" cy="6" r="5" fill="none" stroke="var(--red-deep)" stroke-width="1.3"/><path d="M6 3v3l2 1.5" fill="none" stroke="var(--red-deep)" stroke-width="1.2"/></svg>
      11:30 - 1:00pm // Wednesday, August 24th
    </div>
  </div>

  <div class="benefits">
    <h2>BENEFITS OF DIGITAL INTERVIEWING INCLUDE :</h2>
    <ul>
      <li>Lower Recruiting Costs.</li>
      <li>Higher Quality Talent Pools.</li>
      <li>Screen More Candidates in Less Time.</li>
      <li>Schedule First Round Interviews with only Qualified Candidates.</li>
      <li>Share with Multiple Hiring Managers.</li>
      <li>Reduced Travel Expenses.</li>
      <li>On Demand Flexibility.</li>
    </ul>
  </div>

  <div class="purpose">
    <h2>PRESENTATION PURPOSE:</h2>
    <p>A step-by-step demonstration and an overall introduction to Digital Interviewing and why they have quickly replaced the phone interview and resume.</p>
  </div>

  <div class="contact-rule" style="bottom:112px"></div>
  <div class="contact">
    <div class="email">dana.morrow@rlstaffing.com</div>
    <div class="phone">Or call 615 555-0148 For More Information.</div>
  </div>
</section>

</body>
</html>
```